Velmorix E-commerce Website Design

I'm looking into having my e-comm website built. We are an investment company that is investing in a private label focused on a rising sport category called Pickleball in EU market.

We will provide top quality material and acessories for players be ready to go to courts. We will have a range of: Rackets, Set of balls, Net, Lines, overgrip, water bottle, player bag.

As it´s a new sports category we would like to see an architecture that alows us to share some storytelling about the category, the brand and lead to purchase of our products.

We will position our self as an inclusive and fun brand that you can reach out to find more info about Pickleball Sport, buy your pickleball stuff and have fun. Its all about action and fun.

Target Market(s)

Europe Market

Industry/Entity Type

Pickleball (Sports)

Coding

Coded - Design and coding required

Number of Pages Required

1 page

Requirements
Must have
• E-commerce look and feel
Nice to have
• A bit of storytelling about the brand and specially the category (Pickleball).

```html
<!DOCTYPE html>
<html lang="en">
<head>
<meta charset="utf-8">
<title>Velmorix – Pickleball Gear</title>
<link rel="stylesheet" href="https://fonts.googleapis.com/css2?family=Lato:ital,wght@0,400;0,700;0,900;1,400&family=Poppins:wght@600&display=swap">
<style>
:root{
  --green:#6fbb2c;
  --green-dark:#5ea322;
  --ink:#222;
  --text:#555;
  --light-blue:#dbe3ec;
  --footer:#202020;
  --white:#fff;
}
*{box-sizing:border-box;margin:0;padding:0}
html,body{width:1200px;height:4006px;overflow:hidden}
body{font-family:'Lato',sans-serif;color:var(--text);background:var(--white);position:relative}
a{color:inherit;text-decoration:none}
.btn{display:inline-flex;align-items:center;justify-content:center;background:var(--green);color:var(--white);font-weight:700;font-size:16px}
.section-title{font-family:'Lato',sans-serif;font-weight:900;color:var(--ink);font-size:46px;text-align:center}

.site-header{position:absolute;top:0;left:0;width:1200px;height:104px;display:flex;align-items:center}
.logo{position:absolute;left:73px;font-family:'Poppins',sans-serif;font-weight:600;font-size:36px;color:var(--ink)}
.main-nav{position:absolute;left:338px;display:flex;gap:30px;font-size:13px;font-weight:700;color:#333;text-transform:uppercase;letter-spacing:.2px}
.main-nav .active{color:var(--green);text-decoration:underline}
.cart{display:flex;align-items:center;gap:8px;color:var(--green);position:relative}
.cart-badge{position:absolute;right:-14px;top:-12px;width:16px;height:16px;border-radius:50%;background:var(--green);color:#fff;font-size:10px;display:flex;align-items:center;justify-content:center}

.hero{position:absolute;top:104px;left:0;width:1200px;height:674px;background:radial-gradient(ellipse at 55% 40%,#2e9a4c 0%,#1f8a40 55%,#17753a 100%);text-align:center;color:var(--white)}
.hero-title{position:absolute;top:214px;width:100%;font-weight:900;font-size:68px}
.hero-title span{color:var(--green)}
.hero-sub{position:absolute;top:298px;left:160px;width:880px;font-weight:700;font-size:25px;line-height:31px}
.hero .btn{position:absolute;top:387px;left:515px;width:171px;height:54px;font-size:22px}
.arrow{position:absolute}

.welcome{position:absolute;top:778px;left:0;width:1200px;height:401px;text-align:center}
.welcome .section-title{margin-top:44px}
.welcome p{width:1060px;margin:24px auto 0;font-size:15.5px;line-height:30.5px}
.welcome .btn{margin-top:34px;width:184px;height:48px}

.split{position:absolute;left:0;width:1200px;height:500px;background:var(--light-blue)}
.split .photo{position:absolute;top:0;height:500px;width:660px}
.split h2{font-weight:900;color:var(--ink);font-size:46px}
.split p{font-size:16px;line-height:30.5px;margin-top:18px}
.split .btn{margin-top:34px;width:184px;height:48px}
.what{top:1179px}
.what .photo{left:0;background:linear-gradient(90deg,#2e2a36 0%,#5c6a80 45%,rgba(219,227,236,0) 100%)}
.what .copy{position:absolute;left:615px;top:104px;width:490px}
.about{top:2231px}
.about .photo{right:0;background:linear-gradient(270deg,#3a4454 0%,#6e7f96 45%,rgba(219,227,236,0) 100%)}
.about .copy{position:absolute;left:77px;top:105px;width:500px}

.products{position:absolute;top:1679px;left:0;width:1200px;height:552px}
.products .section-title{margin-top:48px}
.product-list{position:absolute;top:140px;left:75px;display:flex;gap:29px}
.product{width:241px;text-align:center}
.product .thumb{height:195px;border:1px solid #ddd}
.product h3{font-size:18px;font-weight:700;color:var(--ink);margin-top:28px}
.product .price{font-size:18px;margin-top:8px}
.product .btn{width:129px;height:34px;font-size:13px;margin-top:18px}

.testimonials{position:absolute;top:2730px;left:0;width:1200px;height:383px;background:var(--green);color:var(--white)}
.testimonials .section-title{color:var(--white);margin-top:52px}
.avatar{position:absolute;left:257px;top:146px;width:163px;height:163px;border-radius:50%;border:4px solid #e6e6e6;background:linear-gradient(160deg,#8a8a8a,#4a4a4a)}
.quote{position:absolute;left:446px;top:159px;width:500px;font-style:italic;font-size:15.5px;line-height:27px}
.quote-author{position:absolute;left:446px;top:282px;font-weight:700;font-size:16px}

.blog{position:absolute;top:3113px;left:0;width:1200px;height:591px}
.blog .section-title{margin-top:50px}
.blog-list{position:absolute;top:140px;left:75px;display:flex;gap:29px}
.post{width:331px;height:389px;border:1px solid #ddd;text-align:center}
.post .thumb{height:205px}
.post time{display:block;margin-top:28px;font-size:15px;color:var(--ink)}
.post h3{color:var(--green);font-size:21px;font-weight:700;margin-top:8px}
.post p{font-size:15px;line-height:23px;margin:8px auto 0;width:290px}

.site-footer{position:absolute;top:3704px;left:0;width:1200px;height:302px;background:var(--footer);color:#ddd}
.footer-logo{position:absolute;left:73px;top:102px;font-family:'Poppins',sans-serif;font-weight:600;font-size:36px;color:var(--white)}
.copyright{position:absolute;left:75px;top:172px;font-size:12px;line-height:22px}
.footer-col{position:absolute;top:55px}
.footer-col h4{color:var(--white);font-size:17px;font-weight:700;margin-bottom:12px}
.sitemap{left:344px}
.sitemap li{list-style:none;font-size:13.5px;line-height:30px}
.contact{left:518px}
.contact li{list-style:none;display:flex;gap:14px;font-size:14px;line-height:23px;margin-bottom:10px}
.contact svg{flex:none;margin-top:4px}
.signup{left:793px;top:60px}
.signup form{display:flex;margin-top:8px}
.signup .field{width:271px;height:46px;background:var(--white);color:#777;font-size:13px;display:flex;align-items:center;padding-left:16px}
.signup .go{width:61px;height:46px;background:var(--green);display:flex;align-items:center;justify-content:center}
.social{display:flex;gap:18px;margin-top:28px}
.social span{width:20px;height:20px;border-radius:50%;background:#e8e8e8}
</style>
</head>
<body>

<header class="site-header">
  <a class="logo" href="#">Velmorix</a>
  <nav class="main-nav">
    <a class="active" href="#">Home</a>
    <a href="#">Copmpany</a>
    <a href="#">Products</a>
    <a href="#">About Pickleball</a>
    <a href="#">What We Do</a>
    <a href="#">Contact Us</a>
    <a class="cart" href="#">Cart
      <svg width="16" height="14" viewBox="0 0 16 14"><path d="M0 1h3l2 8h9l2-6H4" fill="none" stroke="#333" stroke-width="2"/><circle cx="6" cy="12" r="1.5" fill="#333"/><circle cx="13" cy="12" r="1.5" fill="#333"/></svg>
      <span class="cart-badge">0</span>
    </a>
  </nav>
</header>

<section class="hero" role="img" aria-label="Pickleball paddle and orange ball lying on a green court">
  <svg class="arrow" style="left:40px;top:315px" width="22" height="34" viewBox="0 0 22 34"><path d="M18 3L5 17l13 14" fill="none" stroke="#fff" stroke-width="5"/></svg>
  <svg class="arrow" style="right:40px;top:315px" width="22" height="34" viewBox="0 0 22 34"><path d="M4 3l13 14L4 31" fill="none" stroke="#fff" stroke-width="5"/></svg>
  <h1 class="hero-title">Welcome to <span>Velmorix</span></h1>
  <p class="hero-sub">Vestibulum ante ipsum primis in faucibus orci luctus et ultrices posuere laboris nisi ut aliquip ex ea commodo consequa.</p>
  <a class="btn" href="#">Shop Now</a>
</section>

<section class="welcome">
  <h2 class="section-title">Welcome to Velmorix</h2>
  <p>Lorem ipsum dolor sit amet, consectetur adipiscing elit. Pellentesque rutrum nibh eu nibh porta molestie. Integer elit odio, tincidunt vitae tellus id, &nbsp;laoreet semper purus. Vivamus a tellus eu leo dictum euismod in eu sapien. Suspendisse nec libero tincidunt, aliquet dolor at, pretium erat. Morbi tincidunt erat ac purus commodo interdum. Integer euismod nec dolor ac condimentum. Donec pellentesque orci nec sagittis placerat.</p>
  <a class="btn" href="#">Read More</a>
</section>

<section class="split what">
  <div class="photo" role="img" aria-label="Player in a dark shirt hitting a yellow ball with a paddle"></div>
  <div class="copy">
    <h2>What We Do</h2>
    <p>Lorem ipsum dolor sit amet, consectetur adipiscing elittesque rutrum nibh eu nibh porta molestie. Integer elit odio, &nbsp;tincidunt vitae tellus id, &nbsp;laoreet semper purusivamus a tellus eu leo dictum euismod in eu sapien.</p>
    <a class="btn" href="#">Read More</a>
  </div>
</section>

<section class="products">
  <h2 class="section-title">Our Products</h2>
  <svg class="arrow" style="left:40px;top:281px" width="20" height="32" viewBox="0 0 20 32"><path d="M17 2L4 16l13 14" fill="none" stroke="#333" stroke-width="2.5"/></svg>
  <svg class="arrow" style="right:40px;top:281px" width="20" height="32" viewBox="0 0 20 32"><path d="M3 2l13 14L3 30" fill="none" stroke="#333" stroke-width="2.5"/></svg>
  <div class="product-list">
    <article class="product">
      <div class="thumb" role="img" aria-label="Orange pickleball paddle on a blue court" style="background:linear-gradient(135deg,#4b5ca0,#6a78b8)"></div>
      <h3>Pellentesque aliquet</h3><p class="price">$39.00</p><a class="btn" href="#">Add To Cart</a>
    </article>
    <article class="product">
      <div class="thumb" role="img" aria-label="Pile of colourful pickleball balls" style="background:linear-gradient(135deg,#f2c21e,#e8435d 40%,#41b64a 75%,#2f7fd6)"></div>
      <h3>Pellentesque aliquet</h3><p class="price">$39.00</p><a class="btn" href="#">Add To Cart</a>
    </article>
    <article class="product">
      <div class="thumb" role="img" aria-label="Pickleball court net" style="background:linear-gradient(180deg,#2e3b4a,#3a5a8c 55%,#2f6b4c)"></div>
      <h3>Pellentesque aliquet</h3><p class="price">$39.00</p><a class="btn" href="#">Add To Cart</a>
    </article>
    <article class="product">
      <div class="thumb" role="img" aria-label="Teal sports bag on a sofa" style="background:linear-gradient(180deg,#d9cfc4,#1fa4a8 60%,#c8bfb4)"></div>
      <h3>Pellentesque aliquet</h3><p class="price">$39.00</p><a class="btn" href="#">Add To Cart</a>
    </article>
  </div>
</section>

<section class="split about">
  <div class="photo" role="img" aria-label="Hands holding a paddle and a yellow pickleball ball"></div>
  <div class="copy">
    <h2>About Pickleball Sport</h2>
    <p>Lorem ipsum dolor sit amet, consectetur adipiscing elittesque rutrum nibh eu nibh porta molestie. Integer elit odio, &nbsp;tincidunt vitae tellus id, &nbsp;laoreet semper purusivamus a tellus eu leo dictum euismod in eu sapien.</p>
    <a class="btn" href="#">Read More</a>
  </div>
</section>

<section class="testimonials">
  <h2 class="section-title">Testimonials</h2>
  <svg class="arrow" style="left:212px;top:178px" width="16" height="26" viewBox="0 0 16 26"><path d="M13 2L3 13l10 11" fill="none" stroke="#fff" stroke-width="4"/></svg>
  <svg class="arrow" style="left:974px;top:178px" width="16" height="26" viewBox="0 0 16 26"><path d="M3 2l10 11L3 24" fill="none" stroke="#fff" stroke-width="4"/></svg>
  <div class="avatar" role="img" aria-label="Customer portrait"></div>
  <blockquote class="quote">" Lorem ipsum dolor sit amet, consectetur adipiscing elit neque odio, luctus ac libero eget, accumsan pellentesque felis. Proin ullamcorper tortor vitae sodales efficitur. Pellentesque aliquet augue eget eleifend congue. Integer non lectus mattis..."</blockquote>
  <p class="quote-author">- Name Heading</p>
</section>

<section class="blog">
  <h2 class="section-title">Latest Blog</h2>
  <div class="blog-list">
    <article class="post">
      <div class="thumb" role="img" aria-label="Court net under a blue sky" style="background:linear-gradient(180deg,#7fb6e0,#3f8f95 55%,#6fa86a)"></div>
      <time>Jan12, 2023</time><h3>Neque porro quisquam est qui</h3>
      <p>Morbi tincidunt erat ac purus commodo interdum erat sint occaecat cu pidatat non dicta sunt</p>
    </article>
    <article class="post">
      <div class="thumb" role="img" aria-label="Basket full of yellow balls on court" style="background:linear-gradient(180deg,#2a3550,#3d5f9e 50%,#c9d24a)"></div>
      <time>Jan12, 2023</time><h3>Neque porro quisquam est qui</h3>
      <p>Morbi tincidunt erat ac purus commodo interdum erat sint occaecat cu pidatat non dicta sunt</p>
    </article>
    <article class="post">
      <div class="thumb" role="img" aria-label="Doubles players during a match" style="background:linear-gradient(180deg,#7aa86a,#3f6fae 60%,#5c93c9)"></div>
      <time>Jan12, 2023</time><h3>Neque porro quisquam est qui</h3>
      <p>Morbi tincidunt erat ac purus commodo interdum erat sint occaecat cu pidatat non dicta sunt</p>
    </article>
  </div>
</section>

<footer class="site-footer">
  <div class="footer-logo">Velmorix</div>
  <p class="copyright">Copyright © 2023 Company Name<br>All Right Reserved</p>
  <div class="footer-col sitemap">
    <h4>Site Map</h4>
    <ul><li>Home</li><li>Copmpany</li><li>Products</li><li>About Pickleball</li><li>What We Do</li><li>Contact Us</li></ul>
  </div>
  <div class="footer-col contact">
    <h4>Contact Info</h4>
    <ul>
      <li><svg width="16" height="14" viewBox="0 0 16 14"><path d="M1 2l4-1 6 2 4-1v11l-4 1-6-2-4 1z" fill="var(--green)"/></svg><span>Excepteur sint occaecat<br>Cupidatat aute</span></li>
      <li><svg width="16" height="16" viewBox="0 0 16 16"><path d="M3 1l3 3-2 2c1 2 3 4 6 6l2-2 3 3-2 2C7 14 2 9 1 3z" fill="var(--green)"/></svg><span>1-800-555-0142</span></li>
      <li><svg width="16" height="12" viewBox="0 0 16 12"><rect width="16" height="12" fill="var(--green)"/><path d="M0 0l8 6 8-6" fill="none" stroke="#202020" stroke-width="1.5"/></svg><span>hello@velmorix-shop.com</span></li>
    </ul>
  </div>
  <div class="footer-col signup">
    <h4>Email Sign Up</h4>
    <form>
      <div class="field">Enter Email Address</div>
      <div class="go"><svg width="22" height="20" viewBox="0 0 22 20"><path d="M2 10h16M11 3l7 7-7 7" fill="none" stroke="#fff" stroke-width="4"/></svg></div>
    </form>
    <div class="social"><span></span><span></span><span></span><span></span><span></span></div>
  </div>
</footer>

</body>
</html>
```